Packaging for wooden baby rattles

Hello designers,

We are looking for a great design for our new line of products - Wooden baby rattles.

There will be a few rattle styles that will have one universal packaging.

The packaging will be a window box made with craft paper (natural brown box as shown in the attachment). To add some color to the box, please use the same color as we have in our logo. The color can be used for the frames, symbols, headings etc.

Box size: Length 13cm, Height 10cm, Width 4cm.
Window size: Length 10cm, Height 6cm.

Because the toys are wooden, we want the entire packaging to look natural and eco-friendly. Colors should be in the same family as our logo, which is Pantone color

PACKAGING CONTENT:

TOP OF THE BOX: *leave empty*

BOTTOM OF THE BOX:
*company information shown below and space for the barcode sticker*

NORA & BETH, INC.
52-18 61st Ave.
Jackson Heights
New York, USA
www.noraandbeth-example.com

FRONT OF THE BOX:
Space above the window 2.5cm:
TIMBER PALS by Nora & Beth
* + use Nora & Beth Logo and age recommendation icon for age: 0+ months*
Space below the window 1.5cm:
Safer for the baby, better for the Earth

BACK & SIDES OF THE BOX:
The rest of the content can be distributed on the back and 2 sides of the box:

3 stars indicate the beginning of the segment, 5 stars mean the end of AN IMPORTANT segment. Segments should be prominent and may be placed in individual frames or on the side of the box

***
DEVELOPMENAL TOY
EXPERTLY DESIGNED TO:
- Stimulate baby's senses
- Encourage learning and social skills
- Promote grasping and fine motor skills development
*****

***
All-natural European beechwood
Non-toxic water-based paint
Safe for mouthing and teething
Sustainably harvested
Recyclable
Biodegradable
***
Please use recyclable & biodegradable symbol

ALL NEW MATERIALS:
Natural Beech Wood

CARE INSTRUCTIONS:
Wipe clean with damp cloth. Do not submerge in a water, do not sterilize.

CAUTION:
Packaging may create safety hazard. Remove all packaging, including ribbon ties before entrusting to a child. Adult supervision required. Inspect teether before each use, discard and replace if cracks or tears develop.

Meets and exceeds ASTM, CPSIA and CE toy safety standards

Follow us @noraandbeth on Snapfeed and win great prizes with your Timber Pals

MADE RESPONSIBLY IN CHINA OF WOOD GROWN AND IMPORTED FROM EUROPE

©2016 Nora & Beth, Inc. All rights reserved.

BOTTOM OF THE BOX:

NOT A REQUIREMENT BUT NICE TO HAVE:
The box is for the rattles that will be 4 different characters and a rainbow: please see the attachment. It would be nice to include the sketches of the toys and their names on the box. The design is left up to your creativity.

Characters:
Polly the Puffin, Max the Mole, Rory the Robin, Gina the Gecko + Colorful Rainbow.

Target Market(s)

babies

Industry/Entity Type

Toy Store

Colors
00a990
88d0c7
cfeae6
86cfc6

Requirements
Must have
• Craft Paper Box - brown color as shown in the attachment
Nice to have
• Rattle characters and the rainbow as shown in the attachments:
• Polly the Puffin, Max the Mole, Rory the Robin, Gina the Gecko + the Rainbow.
Should not have
• please do not change the font on the logo

```html
<!DOCTYPE html>
<html lang="en">
<head>
<meta charset="utf-8">
<title>Timber Pals – box dieline</title>
<link rel="stylesheet" href="https://fonts.googleapis.com/css2?family=Josefin+Slab:wght@700&family=PT+Sans:wght@400;700&family=Gochi+Hand&display=swap">
<style>
:root{
  --board:#dcdcdc;
  --edge:#b9b9b9;
  --teal:#1aab8f;
  --teal-mid:#5fc7bb;
  --teal-pale:#a8dcd4;
  --white:#ffffff;
  --ink:#1c1c1c;
  --sans:"PT Sans", Arial, sans-serif;
  --slab:"Josefin Slab", Georgia, serif;
  --hand:"Gochi Hand", "Comic Sans MS", cursive;
}
*{margin:0;padding:0;box-sizing:border-box}
html,body{width:1200px;height:994px;overflow:hidden;background:var(--white)}
.dieline{position:relative;width:1200px;height:994px;font-family:var(--sans);color:var(--ink)}
.dieline svg{position:absolute;left:0;top:0}
.abs{position:absolute}
.brand-mark{display:flex;flex-direction:column;align-items:center;gap:5px;font-size:10px;letter-spacing:.2px}
.brand-mark .dot{width:26px;height:26px;border-radius:50%;background:var(--teal)}
.side-frame{border:1.5px solid var(--teal);border-radius:7px;text-align:center;font-size:8.2px;line-height:13px;padding:26px 3px 0}
.side-frame p{margin-bottom:13px}
.side-frame.facts{padding-top:22px}
.side-frame.facts p{margin:0}
.eco-badges{display:flex;justify-content:center;gap:6px;margin-top:16px}
.eco-badges span{width:36px;height:36px;border-radius:50%;border:1.5px solid #444}
.title{left:150px;width:424px;top:224px;text-align:center;font-family:var(--slab);font-size:36px;letter-spacing:3px;line-height:1}
.byline{left:150px;width:424px;top:262px;text-align:center;font-size:14px}
.window{left:200px;top:284px;width:328px;height:196px;background:var(--white);border:4px solid var(--teal);border-radius:18px}
.tagline{left:150px;width:424px;top:486px;text-align:center;font-family:var(--hand);font-size:18px}
.age{left:526px;top:474px;width:44px;height:44px;border-radius:50%;background:var(--teal);border:1px dashed var(--white);color:var(--white);text-align:center;line-height:1}
.age b{display:block;font-size:20px;font-weight:400;margin-top:6px}
.age small{display:block;font-size:5px}
.characters{left:713px;top:224px;display:flex;gap:4px}
.character{width:78px;height:70px;border:1.5px solid var(--ink);border-radius:6px;display:flex;flex-direction:column;align-items:center;justify-content:flex-end;padding:0 2px 3px}
.character .sketch{width:50px;height:40px;border-radius:14px;background:#9a9a9a;margin-bottom:4px}
.character span{font-family:var(--hand);font-size:9.5px;white-space:nowrap}
.back-copy{left:720px;width:400px;top:310px;text-align:center;font-size:7.4px;line-height:9.5px}
.back-copy p{margin-bottom:10px}
.address{left:730px;top:560px;font-size:7.4px;line-height:12.5px}
</style>
</head>
<body>
<main class="dieline">
  <svg width="1200" height="994" viewBox="0 0 1200 994" aria-hidden="true">
    <defs>
      <linearGradient id="waves" x1="0" y1="0" x2="0" y2="1">
        <stop offset="0" stop-color="#5fc7bb"/>
        <stop offset=".35" stop-color="#1aab8f"/>
        <stop offset=".6" stop-color="#88d0c7"/>
        <stop offset="1" stop-color="#1aab8f"/>
      </linearGradient>
    </defs>
    <g fill="var(--board)" stroke="var(--edge)" stroke-width=".6">
      <polygon points="150,74 164,24 564,24 574,74"/>
      <polygon points="21,203 44,106 150,106 150,203"/>
      <polygon points="21,528 150,528 150,626 44,626"/>
      <polygon points="574,106 681,106 704,203 574,203"/>
      <polygon points="574,528 704,528 681,626 574,626"/>
      <rect x="21" y="203" width="129" height="325"/>
      <rect x="150" y="203" width="424" height="325"/>
      <rect x="574" y="203" width="130" height="325"/>
      <rect x="704" y="203" width="424" height="338"/>
      <polygon points="1128,208 1178,222 1178,515 1128,528"/>
      <rect x="704" y="541" width="424" height="120"/>
      <polygon points="704,661 1128,661 1112,708 720,708"/>
      <rect x="150" y="642" width="424" height="328"/>
    </g>
    <!-- bands -->
    <rect x="21" y="203" width="1107" height="11" fill="var(--teal)"/>
    <rect x="21" y="214" width="1107" height="4" fill="var(--teal-pale)"/>
    <rect x="21" y="505" width="129" height="23" fill="var(--teal)"/>
    <rect x="21" y="500" width="129" height="5" fill="var(--teal-pale)"/>
    <rect x="574" y="505" width="554" height="16" fill="var(--teal)"/>
    <rect x="574" y="500" width="554" height="5" fill="var(--teal-pale)"/>
    <rect x="704" y="521" width="424" height="20" fill="var(--teal-mid)"/>
    <rect x="704" y="640" width="424" height="21" fill="var(--teal-mid)"/>
    <rect x="150" y="642" width="424" height="14" fill="var(--teal-pale)"/>
    <rect x="150" y="656" width="424" height="28" fill="var(--teal)"/>
  </svg>

  <div class="abs" role="img" aria-label="Layered teal wave pattern with dotted lines" style="left:150px;top:74px;width:424px;height:129px;background:linear-gradient(#5fc7bb,#1aab8f 30%,#88d0c7 55%,#5fc7bb 80%,#1aab8f)"></div>
  <div class="abs" role="img" aria-label="Teal wave pattern band" style="left:150px;top:424px;width:424px;height:104px;background:linear-gradient(#88d0c7,#1aab8f 40%,#5fc7bb 70%,#1aab8f)"></div>

  <!-- left side -->
  <div class="abs brand-mark" style="left:21px;top:228px;width:129px"><span class="dot"></span>NORA &amp; BETH</div>
  <div class="abs side-frame" style="left:30px;top:280px;width:112px;height:194px">
    <p>DEVELOPMENAL TOY<br>EXPERTLY DESIGNED TO:</p>
    <p>Stimulate baby's senses</p>
    <p>Encourage learning and social skills</p>
    <p>Promote grasping and fine motor skills development</p>
  </div>

  <!-- front -->
  <h1 class="abs title">TIMBER PALS</h1>
  <div class="abs byline">by NORA &amp; BETH</div>
  <div class="abs window"></div>
  <div class="abs tagline">Safer for the baby, better for the Earth</div>
  <div class="abs age"><b>0+</b><small>month</small></div>

  <!-- right side -->
  <div class="abs brand-mark" style="left:574px;top:228px;width:130px"><span class="dot"></span>NORA &amp; BETH</div>
  <div class="abs side-frame facts" style="left:584px;top:280px;width:112px;height:194px">
    <p>All-natural European beechwood</p>
    <p>Non-toxic water-based paint</p>
    <p>Safe for mouthing and teething</p>
    <p>Sustainably harvested</p>
    <p>Recyclable</p>
    <p>Biodegradable</p>
    <div class="eco-badges"><span></span><span></span></div>
  </div>

  <!-- back -->
  <div class="abs characters">
    <div class="character"><div class="sketch" role="img" aria-label="Sketch of the puffin rattle"></div><span>Polly the Puffin</span></div>
    <div class="character"><div class="sketch" role="img" aria-label="Sketch of the mole rattle"></div><span>Max the Mole</span></div>
    <div class="character"><div class="sketch" role="img" aria-label="Sketch of the robin rattle"></div><span>Rory the Robin</span></div>
    <div class="character"><div class="sketch" role="img" aria-label="Sketch of the gecko rattle"></div><span>Gina the Gecko</span></div>
    <div class="character"><div class="sketch" role="img" aria-label="Sketch of the rainbow rattle"></div><span>The rainbow</span></div>
  </div>
  <div class="abs back-copy">
    <p>ALL NEW MATERIALS:<br>Natural Beech Wood</p>
    <p>CARE INSTRUCTIONS:<br>Wipe clean with damp cloth. Do not submerge in a water, do not sterilize.</p>
    <p>CAUTION:<br>Packaging may create safety hazard. Remove all packaging, including ribbon ties<br>before entrusting to a child. Adult supervision required. Inspect teether before<br>each use, discard and replace if cracks or tears develop.</p>
    <p>Meets and exceeds ASTM, CPSIA and CE toy safety standards</p>
    <p>Follow us @noraandbeth on Snapfeed and win great prizes with your Timber Pals</p>
    <p>MADE RESPONSIBLY IN CHINA OF WOOD GROWN AND IMPORTED FROM EUROPE</p>
    <p>©2016 Nora &amp; Beth, Inc. All rights reserved.</p>
  </div>

  <!-- bottom -->
  <address class="abs address" style="font-style:normal">
    NORA &amp; BETH, INC.<br>52-18 61st Ave.<br>Jackson Heights<br>New York, USA<br>www.noraandbeth-example.com
  </address>
</main>
</body>
</html>
```